Buch-/eBook-Cover für Sachbuch gesucht
Zielgruppe
We're selfpublishing nonfiction books. Interested are adults - mostly man (age range: 25-50) - who want to learn more about leadership at their workplaces.
Aufgabenstellung
The design should be clean and simple, title easy to read, good color contrast (the cover has to stand out from an white background).

```html
<!DOCTYPE html>
<html lang="en">
<head>
<meta charset="utf-8">
<title>Leadership – Book Cover</title>
<link rel="stylesheet" href="https://fonts.googleapis.com/css2?family=Open+Sans:wght@800&family=Fira+Sans+Condensed:wght@500;600&display=swap">
<style>
  :root {
    --paper: #f1f4f5;
    --navy: #2b3f63;
    --aqua: #92d0dc;
    --red: #d42a33;
    --author: #7fc7d5;
    --sky-deep: #8ec9e6;
    --sky-light: #cfe8f2;
    --cloud: #e9f2f5;
  }
  * { margin: 0; padding: 0; box-sizing: border-box; }
  html, body { width: 848px; height: 1200px; overflow: hidden; }
  body { background: var(--paper); }
  .cover {
    position: relative;
    width: 848px;
    height: 1200px;
    overflow: hidden;
    background: var(--paper);
  }
  .title { font-weight: inherit; }
  .title-top {
    position: absolute;
    left: 86px;
    top: 60px;
    font-family: "Open Sans", sans-serif;
    font-weight: 800;
    font-size: 200px;
    line-height: 1;
    letter-spacing: -19px;
    color: var(--navy);
    white-space: nowrap;
  }
  .title-bottom {
    position: absolute;
    left: 48px;
    top: 200px;
    font-family: "Open Sans", sans-serif;
    font-weight: 800;
    font-size: 350px;
    line-height: 1;
    letter-spacing: -25px;
    color: var(--aqua);
    text-shadow: 2px 2px 0 var(--navy);
    white-space: nowrap;
  }
  .subtitle {
    position: absolute;
    left: 170px;
    top: 532px;
    font-family: "Fira Sans Condensed", sans-serif;
    font-weight: 600;
    color: var(--red);
    line-height: 0.98;
    white-space: nowrap;
  }
  .subtitle .line { display: block; font-size: 66px; }
  .subtitle .line-two { margin-top: -4px; }
  .subtitle .joiner { font-size: 32px; vertical-align: 26px; margin-right: 6px; }
  .illustration {
    position: absolute;
    left: 0;
    top: 740px;
    width: 848px;
    height: 460px;
    background:
      linear-gradient(90deg, var(--sky-deep) 0%, var(--sky-light) 45%, var(--cloud) 62%, var(--paper) 100%);
  }
  .author {
    position: absolute;
    left: 520px;
    top: 982px;
    font-family: "Fira Sans Condensed", sans-serif;
    font-weight: 500;
    font-size: 70px;
    line-height: 0.95;
    letter-spacing: -1px;
    color: var(--author);
    white-space: nowrap;
  }
</style>
</head>
<body>
  <main class="cover">
    <div class="illustration" role="img" aria-label="Paper-cut sky with layered clouds and a flock of white paper planes led by one red paper plane"></div>
    <h1 class="title">
      <span class="title-top">LEADER</span>
      <span class="title-bottom">SHIP</span>
    </h1>
    <p class="subtitle">
      <span class="line">Fostering Growth</span>
      <span class="line line-two"><span class="joiner">and</span>Inspiring Excellence</span>
    </p>
    <p class="author">Daniel<br>Whitmore</p>
  </main>
</body>
</html>
```